Trendo - Forex Signal Services Momentum Matters Most. Shape your path.

I need an attractive eye catching Hub page that is user friendly.  Both fun and professional.
I have attached a copy of my website design (not completed) for an idea what I want.
Trendo is a highly reputable, trustworthy and professional site that offers forex signals to traders in all parts of the globe. With accurate and reliable forex signals, traders can not only make money but also boost their profits.
At Trendo, we want our clients to have complete faith on us and our services! We also do not want our users to lead a simple and monotonous life.  Instead our goal is to help them create an extra source of steady income. However, this is possible only when our clients resolve to change their lives for the better. They need to change their mindset and most importantly develop a positive frame of mind. That’s exactly why at Trendo, we provide our clients with innumerable personal development tools and resources that’ll aid them in changing all the aspects of their lives. We want our traders to feel inspired and educate them in the right way!
Colors are flexible.

Target Market(s)
I work with Forex Traders, Investors wanting to control their own portfolios, and work from home entrepreneurs.
Industry/Entity Type
It Professional
Requirements
Must have
- It must have a professional clean look. I want this page to be interactive and eye catching. I want my audience hooked within seconds of opening it. It has to have all important information first. Photos must be legit and not spammy. I work as a representative in the financial market. I want my page to reflect that I stand by my product and reputation means everything to me. This site has to be engaging.

Should not have
- Not white collar conservative

```html
<!DOCTYPE html>
<html lang="en">
<head>
<meta charset="utf-8">
<title>Trendo – Forex Signal Services Page</title>
<link rel="stylesheet" href="https://fonts.googleapis.com/css2?family=Montserrat:wght@300;400;700&family=Roboto:wght@400;500;700&display=swap">
<style>
  :root {
    --canvas-white: #ffffff;
    --page-bg: #e9ebee;
    --bar-blue: #3b5998;
    --bar-line: #29487d;
    --nav-accent: #4267b2;
    --action-blue: #4080ff;
    --text-dark: #1d2129;
    --text-muted: #4b4f56;
    --border-grey: #ccd0d5;
    --panel-black: #000000;
    --brand-orange: #f7931e;
    --accent-orange: #f28a1f;
    --text-white: #ffffff;
    --city-deep: #0a1230;
    --city-mid: #1d3a7a;
    --city-glow: #2fc6f0;
    --city-violet: #6a3bd6;
    --avatar-tone: #8a6a5a;
  }
  html, body {
    margin: 0; padding: 0;
    width: 1200px; height: 768px;
    overflow: hidden;
    background: var(--canvas-white);
    font-family: "Roboto", Arial, sans-serif;
  }
  .stage { position: relative; width: 1200px; height: 768px; }

  /* top bar */
  .topbar {
    position: absolute; left: 60px; top: 211px;
    width: 1080px; height: 34px;
    background: var(--bar-blue);
    border-bottom: 1px solid var(--bar-line);
  }
  .network-name {
    position: absolute; left: 118px; top: 9px;
    color: var(--text-white); font-weight: 700; font-size: 13px; line-height: 16px;
  }
  .search-box {
    position: absolute; left: 146px; top: 6px;
    width: 356px; height: 19px;
    background: var(--canvas-white); border-radius: 2px;
    font-size: 12px; line-height: 19px; color: var(--text-dark);
    box-sizing: border-box; padding-left: 8px;
  }
  .search-button {
    position: absolute; right: 0; top: 0; width: 37px; height: 19px;
    background: #f6f7f9; border-left: 1px solid #dddfe2;
  }
  .search-button svg { position: absolute; left: 13px; top: 4px; }
  .user-chip {
    position: absolute; left: 659px; top: 6px; height: 18px;
    display: flex; align-items: center; gap: 6px;
    color: var(--text-white); font-weight: 700; font-size: 10.5px;
  }
  .user-avatar { width: 17px; height: 17px; background: var(--avatar-tone); display: block; }
  .bar-divider { width: 1px; height: 16px; background: var(--bar-line); margin: 0 6px; }
  .bar-icons { position: absolute; left: 801px; top: 8px; }

  /* page body */
  .page-body {
    position: absolute; left: 60px; top: 246px;
    width: 1080px; height: 311px;
    background: var(--page-bg);
  }
  .profile-card {
    position: absolute; left: 180px; top: 255px;
    width: 134px; height: 134px;
    background: var(--canvas-white);
    border: 1px solid #dddfe2; border-radius: 2px;
    box-sizing: border-box; padding: 3px;
  }
  .profile-inner {
    width: 100%; height: 100%;
    border: 1px solid #dddfe2; box-sizing: border-box;
    display: flex; flex-direction: column; align-items: center; justify-content: center; gap: 8px;
  }
  .profile-dot { width: 40px; height: 40px; border-radius: 50%; background: var(--brand-orange); }
  .profile-name {
    font-family: "Montserrat", sans-serif; font-weight: 300;
    font-size: 24px; letter-spacing: 2px; color: var(--brand-orange); line-height: 1;
  }
  .page-nav { position: absolute; left: 178px; top: 414px; width: 141px; }
  .page-nav a {
    display: block; height: 25px; line-height: 25px;
    padding-left: 8px; font-size: 12px; color: var(--text-muted); text-decoration: none;
  }
  .page-nav a.is-active {
    background: #dddfe2; color: var(--text-dark); font-weight: 500;
    border-left: 2px solid var(--nav-accent); padding-left: 6px;
  }

  /* cover and action strip */
  .cover { position: absolute; left: 326px; top: 246px; width: 663px; height: 252px; display: block; }
  .action-strip {
    position: absolute; left: 326px; top: 498px;
    width: 663px; height: 40px;
    background: var(--canvas-white);
    border: 1px solid #dddfe2; border-top: none; box-sizing: border-box;
  }
  .action-group {
    position: absolute; left: 10px; top: 8px; height: 23px;
    display: flex; border: 1px solid var(--border-grey); border-radius: 2px;
    background: #f6f7f9; box-sizing: border-box;
  }
  .action-group span {
    display: flex; align-items: center; gap: 4px;
    padding: 0 9px; font-size: 10px; font-weight: 700; color: var(--text-muted);
  }
  .action-group span + span { border-left: 1px solid var(--border-grey); }
  .action-liked { width: 50px; color: var(--nav-accent) !important; }
  .action-message { width: 56px; }
  .action-more { width: 50px; }
  .contact-button {
    position: absolute; left: 413px; top: 8px;
    width: 239px; height: 22px;
    background: var(--action-blue); border-radius: 2px;
    color: var(--text-white); font-size: 12px; line-height: 22px; text-align: center;
  }

  /* cover type */
  .headline { font-family: "Montserrat", sans-serif; font-weight: 700; font-size: 34px; letter-spacing: -1px; }
  .headline .accent { fill: var(--brand-orange); }
  .headline .plain { fill: var(--text-white); }
  .tagline { font-family: "Montserrat", sans-serif; font-weight: 400; font-size: 17px; fill: var(--text-white); }
  .brand-name { font-family: "Montserrat", sans-serif; font-weight: 300; font-size: 38px; letter-spacing: 3px; fill: var(--brand-orange); }
  .brand-line { font-family: "Montserrat", sans-serif; font-weight: 300; font-size: 9px; letter-spacing: 3px; fill: var(--brand-orange); }
</style>
</head>
<body>
<main class="stage">
  <header class="topbar">
    <span class="network-name">Hub</span>
    <div class="search-box">MockupVault.com
      <span class="search-button">
        <svg width="11" height="11" viewBox="0 0 11 11"><circle cx="4.5" cy="4.5" r="3.5" fill="none" stroke="#4b4f56" stroke-width="1.3"/><line x1="7" y1="7" x2="10" y2="10" stroke="#4b4f56" stroke-width="1.3"/></svg>
      </span>
    </div>
    <div class="user-chip">
      <span class="user-avatar" role="img" aria-label="Profile photo"></span>
      <span>Alex Rowan</span>
      <span class="bar-divider"></span>
      <span>Home</span>
    </div>
    <svg class="bar-icons" width="200" height="18" viewBox="0 0 200 18">
      <g fill="#ffffff">
        <circle cx="14" cy="4" r="3.2"/><path d="M8,16 Q8,8 14,8 Q20,8 20,16 Z"/>
        <circle cx="7" cy="5" r="2.6"/><path d="M2,15 Q2,9 7,9 Q10,9 11,11 L10,15 Z"/>
        <path d="M39,3 H53 V11 H45 L41,14 V11 H39 Z"/><path d="M35,6 H38 V12 H40 V14 L37,16 V14 H35 Z"/>
        <circle cx="71" cy="8" r="7.5"/>
      </g>
      <path d="M66,5 Q70,6 69,9 Q72,11 70,14 M74,2 Q72,5 75,7 Q77,9 76,12" fill="none" stroke="#3b5998" stroke-width="1.6"/>
      <line x1="104" y1="0" x2="104" y2="16" stroke="#29487d"/>
      <g fill="#ffffff">
        <rect x="158" y="5" width="6" height="7"/><rect x="165" y="6" width="6" height="1.5"/><rect x="165" y="9" width="6" height="1.5"/>
        <path d="M178,7 H186 L182,11 Z"/>
      </g>
    </svg>
  </header>

  <section class="page-body"></section>

  <aside>
    <div class="profile-card">
      <div class="profile-inner">
        <span class="profile-dot"></span>
        <span class="profile-name">Trendo</span>
      </div>
    </div>
    <nav class="page-nav">
      <a class="is-active">Home</a>
      <a>Photos</a>
      <a>Likes</a>
    </nav>
  </aside>

  <svg class="cover" viewBox="0 0 828 315" xmlns="http://www.w3.org/2000/svg" aria-label="Trendo Forex Signal Services cover">
    <defs>
      <linearGradient id="city-tones" x1="0" y1="1" x2="1" y2="0">
        <stop offset="0" stop-color="var(--city-deep)"/>
        <stop offset="0.45" stop-color="var(--city-mid)"/>
        <stop offset="0.75" stop-color="var(--city-violet)"/>
        <stop offset="1" stop-color="var(--city-glow)"/>
      </linearGradient>
    </defs>
    <rect x="0" y="0" width="828" height="315" fill="var(--panel-black)"/>
    <path class="city-photo" role="img" aria-label="Night city skyline overlaid with glowing blue market chart lines"
          d="M346,0 Q298,157 364,315 L828,315 L828,0 Z" fill="url(#city-tones)"/>
    <path class="divider-arc" d="M340,0 Q290,157 358,315" fill="none" stroke="var(--accent-orange)" stroke-width="8"/>
    <text class="headline" x="154" y="107" text-anchor="middle"><tspan class="accent">FOREX</tspan><tspan class="plain"> SIGNAL</tspan></text>
    <text class="headline plain" x="154" y="143" text-anchor="middle" fill="var(--text-white)">SERVICES</text>
    <text class="tagline" x="154" y="173" text-anchor="middle">Momentum Matters Most</text>
    <circle cx="62" cy="242" r="22" fill="var(--brand-orange)"/>
    <text class="brand-name" x="100" y="256">Trendo</text>
    <text class="brand-line" x="102" y="276">SHAPE YOUR PATH</text>
  </svg>

  <div class="action-strip">
    <div class="action-group">
      <span class="action-liked">
        <svg width="10" height="10" viewBox="0 0 10 10"><rect x="0" y="4" width="2.5" height="6" fill="#4267b2"/><path d="M3.5,4 L6,0 Q7.5,0 7,3 H10 V6 L8.5,10 H3.5 Z" fill="#4267b2"/></svg>
        Liked ▾
      </span>
      <span class="action-message">
        <svg width="10" height="10" viewBox="0 0 10 10"><circle cx="5" cy="5" r="5" fill="#90949c"/></svg>
        Message
      </span>
      <span class="action-more">··· More ▾</span>
    </div>
    <div class="contact-button">Contact Us</div>
  </div>
</main>
</body>
</html>
```